Post storm repair flyer

looking for an eye catching 6x9 postcard to send out to single family home owners advertising a "Post Storm Repair Special" explaining that after the recent hurricanes its very important to have your roof checked and any repairs fixed right away before they become a bigger more costly problem and that even though your home wasn't directly hit by the storm the high wind gust could've cause unseen damage.
offer $200 off any repair *some rules may apply
Crest Roofing
877.612.LOFT
www.LoftRoofingco.example

```html
<!DOCTYPE html>
<html lang="en">
<head>
<meta charset="utf-8">
<title>Crest Roofing – Post Storm Repair Special Postcard</title>
<link href="https://fonts.googleapis.com/css2?family=Jost:wght@500;600;700&family=Poppins:wght@400;500&display=swap" rel="stylesheet">
<style>
  :root {
    --backdrop: #654c0a;
    --ink: #0a0a0a;
    --paper: #ffffff;
    --paper-shade: #ececec;
    --gold: #fdbf12;
    --roof-sky: #a9c6e2;
    --roof-slate: #4b5566;
    --roof-dark: #2b3240;
    --muted-white: #e9e9e9;
  }
  * { margin: 0; padding: 0; box-sizing: border-box; }
  html, body { width: 1200px; height: 1200px; overflow: hidden; }
  body { background: var(--backdrop); position: relative; font-family: "Poppins", sans-serif; }

  .postcard {
    position: absolute; top: 215px; width: 513px; height: 769px; overflow: hidden;
    background: linear-gradient(135deg, var(--paper) 0%, var(--paper-shade) 55%, var(--paper) 100%);
    box-shadow: 0 6px 14px rgba(0,0,0,.3);
  }
  .postcard--front { left: 58px; }
  .postcard--back { left: 628px; width: 514px; }
  .postcard svg.shapes { position: absolute; inset: 0; width: 100%; height: 100%; }

  .brand { position: absolute; left: 40px; top: 86px; display: flex; align-items: center; gap: 8px; }
  .brand__mark { width: 14px; height: 14px; background: var(--ink); }
  .brand__name { font-family: "Jost", sans-serif; font-weight: 700; font-size: 22px; color: var(--ink); letter-spacing: .5px; }
  .website { position: absolute; left: 40px; top: 152px; font-family: "Jost", sans-serif; font-weight: 500; font-size: 13px; color: var(--ink); letter-spacing: .3px; }

  .headline { position: absolute; left: 32px; top: 196px; font-family: "Jost", sans-serif; font-weight: 700; color: var(--ink); line-height: 1; }
  .headline__kicker { display: block; font-size: 38px; letter-spacing: -.5px; }
  .headline__main { display: block; font-size: 64px; letter-spacing: -1.5px; line-height: .84; margin-top: 6px; }

  .storm-note { position: absolute; left: 40px; top: 394px; width: 410px; font-size: 13.4px; line-height: 18px; color: var(--paper); }

  .offer { position: absolute; left: 114px; top: 538px; width: 284px; height: 59px; display: flex; align-items: center; justify-content: center; font-family: "Jost", sans-serif; font-weight: 700; font-size: 50px; color: var(--gold); letter-spacing: -.5px; }
  .offer-sub { position: absolute; left: 0; right: 0; top: 608px; text-align: center; font-family: "Jost", sans-serif; font-weight: 700; font-size: 40px; color: var(--ink); letter-spacing: -.5px; }
  .fine-print { position: absolute; left: 0; right: 0; top: 660px; text-align: center; font-size: 14px; color: var(--ink); }

  .phone { position: absolute; left: 43px; top: 726px; display: flex; align-items: center; gap: 11px; }
  .phone svg { width: 28px; height: 28px; }
  .phone__number { font-family: "Jost", sans-serif; font-weight: 600; font-size: 21px; color: var(--ink); }

  .why-title { position: absolute; left: 48px; top: 92px; font-family: "Jost", sans-serif; font-weight: 700; font-size: 40px; line-height: 33px; color: var(--paper); letter-spacing: -.3px; }
  .benefits { position: absolute; left: 48px; top: 182px; list-style: none; }
  .benefits li { display: flex; align-items: center; gap: 14px; height: 27.3px; font-size: 16.5px; color: var(--muted-white); }
  .benefits svg { width: 18px; height: 18px; flex: none; }
</style>
</head>
<body>

<section class="postcard postcard--front" aria-label="Postcard front">
  <svg class="shapes" viewBox="0 0 513 769" aria-hidden="false">
    <defs>
      <linearGradient id="roofTone" x1="0" y1="0" x2="1" y2="1">
        <stop offset="0" stop-color="var(--roof-sky)"/>
        <stop offset=".35" stop-color="var(--roof-slate)"/>
        <stop offset="1" stop-color="var(--roof-dark)"/>
      </linearGradient>
    </defs>
    <polygon points="0,0 106,0 94,40 0,40" fill="var(--ink)"/>
    <g role="img" aria-label="Photo of a house roof with grey asphalt shingles under a blue sky">
      <polygon points="219,0 513,0 513,9 447,121 312,121" fill="url(#roofTone)"/>
      <polygon points="513,24 450,128 503,231 513,246" fill="url(#roofTone)"/>
      <polygon points="315,129 439,129 495,233 439,337 315,337 259,233" fill="url(#roofTone)"/>
    </g>
    <polygon points="0,385 501,385 464,496 0,496" fill="var(--gold)"/>
    <polygon points="0,379 494,379 458,489 0,489" fill="var(--ink)"/>
    <rect x="0" y="548" width="513" height="40" fill="var(--gold)"/>
    <polygon points="114,538 398,538 379,597 132,597" fill="var(--ink)"/>
    <polygon points="293,727 513,727 513,769 279,769" fill="var(--gold)"/>
  </svg>

  <div class="brand"><span class="brand__mark"></span><span class="brand__name">CREST ROOFING</span></div>
  <p class="website">LOFTROOFINGCO.EXAMPLE</p>

  <h1 class="headline">
    <span class="headline__kicker">POST STORM</span>
    <span class="headline__main">REPAIR<br>SPECIAL</span>
  </h1>

  <p class="storm-note">After the recent hurricanes, it's crucial to have your roof inspected and any damage repaired promptly. Even if your home wasn't directly hit, high wind gusts could have caused unseen damage.</p>

  <div class="offer">$200 OFF</div>
  <p class="offer-sub">ANY REPAIR</p>
  <p class="fine-print">*some rules may apply</p>

  <div class="phone">
    <svg viewBox="0 0 28 28" aria-hidden="true">
      <circle cx="14" cy="14" r="14" fill="var(--gold)"/>
      <path d="M10.2 7.5c.6-.4 1.3-.2 1.6.4l1.3 2.4c.3.6.1 1.2-.4 1.6l-.9.7c.7 1.6 1.9 2.8 3.5 3.6l.7-.9c.4-.5 1.1-.7 1.6-.4l2.4 1.3c.6.3.8 1.1.4 1.6l-.9 1.3c-.5.7-1.4 1-2.2.7-4-1.4-6.9-4.3-8.3-8.3-.3-.8 0-1.7.7-2.2z" fill="var(--paper)"/>
    </svg>
    <span class="phone__number">877.612.LOFT</span>
  </div>
</section>

<section class="postcard postcard--back" aria-label="Postcard back">
  <svg class="shapes" viewBox="0 0 514 769">
    <defs>
      <linearGradient id="backDark" x1="0" y1="0" x2="1" y2="1">
        <stop offset="0" stop-color="#050505"/>
        <stop offset=".6" stop-color="#1c1c1c"/>
        <stop offset="1" stop-color="#0b0b0b"/>
      </linearGradient>
    </defs>
    <polygon points="0,0 514,0 514,496 0,419" fill="url(#backDark)"/>
    <polygon points="0,419 514,496 514,505 0,428" fill="var(--gold)"/>
    <polygon points="0,0 153,0 145,29 0,29" fill="var(--gold)"/>
    <rect x="58" y="476" width="82" height="91" fill="none" stroke="var(--ink)" stroke-width="1.5"/>
    <g stroke="#3a3a3a" stroke-width="1.4">
      <line x1="58" y1="612" x2="455" y2="612"/>
      <line x1="58" y1="650" x2="455" y2="650"/>
      <line x1="58" y1="691" x2="455" y2="691"/>
      <line x1="58" y1="730" x2="455" y2="730"/>
    </g>
    <polygon points="182,756 514,756 514,769 177,769" fill="var(--gold)"/>
  </svg>

  <h2 class="why-title">WHY CHOOSE CREST<br>ROOFING?</h2>
  <ul class="benefits">
    <li><svg viewBox="0 0 18 18" aria-hidden="true"><circle cx="9" cy="9" r="9" fill="var(--gold)"/><path d="M5 9.2l2.7 2.6L13 6.5" fill="none" stroke="var(--ink)" stroke-width="2"/></svg>licensed roofing professionals</li>
    <li><svg viewBox="0 0 18 18" aria-hidden="true"><circle cx="9" cy="9" r="9" fill="var(--gold)"/><path d="M5 9.2l2.7 2.6L13 6.5" fill="none" stroke="var(--ink)" stroke-width="2"/></svg>Quality materials</li>
    <li><svg viewBox="0 0 18 18" aria-hidden="true"><circle cx="9" cy="9" r="9" fill="var(--gold)"/><path d="M5 9.2l2.7 2.6L13 6.5" fill="none" stroke="var(--ink)" stroke-width="2"/></svg>Free roof inspections</li>
    <li><svg viewBox="0 0 18 18" aria-hidden="true"><circle cx="9" cy="9" r="9" fill="var(--gold)"/><path d="M5 9.2l2.7 2.6L13 6.5" fill="none" stroke="var(--ink)" stroke-width="2"/></svg>Competitive pricing</li>
    <li><svg viewBox="0 0 18 18" aria-hidden="true"><circle cx="9" cy="9" r="9" fill="var(--gold)"/><path d="M5 9.2l2.7 2.6L13 6.5" fill="none" stroke="var(--ink)" stroke-width="2"/></svg>Excellent services</li>
  </ul>
</section>

</body>
</html>
```